Website will be built in Dot Net Nuke v5 so fonts used need to be system fonts and design needs to be convertible to DNN skins/containers.
There is an existing website www.tallowwraps.com.au that we are redesigning with a more updated look based on the below but we are open to deviations or suggestions as to layout.
Site Map
o Home
o Health/Nutrition
o Store Locator
o Products
o Leasing
o Partners
o About Us
o Contact Us
Marlow Design Brief
Colours: Purple and Orange as per attached logo
The website will be purely targeted to the consumer but also allow for franchise enquiry and access for leasing agents. It also needs to portray corporate credibility.
Homepage and a content page will be mocked up with dummy content (have attached some images that can be used)
Design needs to be fresh and funky, young, vibrant with a cool flash section on the homepage
Homepage design requirements:
- Top Left Corner - Marlow Wraps logo
- Next to the logo – a banner with the words “It's how we roll"
- Left Pane (Narrow) – 2 call to action buttons – Franchise Enquiry and Store Locator
- Middle Content Pane – Funky flash area with rotating images that roll away like a kebab to reveal the next image.
- Below Middle Content Pane – Latest News on left and some content on the right
- Right Pane – Logos of clients vertically
Footer - Website Design by BRISK Digital and Privacy Statement, Terms of Use, Login etc that are standard with Dot Net Nuke

```html
<!DOCTYPE html>
<html lang="en">
<head>
<meta charset="utf-8">
<title>Marlow Wraps – It's how we roll</title>
<link href="https://fonts.googleapis.com/css2?family=Arimo:wght@400;700&display=swap" rel="stylesheet">
<style>
:root{
  --purple:#4a0a86;
  --purple-mid:#6a20ad;
  --purple-text:#4b0f8c;
  --orange:#f07d12;
  --orange-deep:#c9650d;
  --white:#ffffff;
  --ink:#2a2a2a;
  --grey-bg:#e6e6e6;
  --rule:#d0d0d0;
}
*{margin:0;padding:0;box-sizing:border-box}
html,body{width:1200px;height:966px;overflow:hidden}
body{
  position:relative;
  font-family:"Arimo",Arial,sans-serif;
  color:var(--ink);
  background:linear-gradient(to bottom,var(--purple) 0,var(--purple) 430px,#b9a5cf 520px,var(--grey-bg) 600px,var(--grey-bg) 100%);
}
.topbar{position:absolute;left:0;top:0;width:1200px;height:70px;background:linear-gradient(to bottom,#7226b4,var(--purple-mid))}
.navbar{position:absolute;left:0;top:70px;width:1200px;height:38px;background:var(--orange)}
.brand{position:absolute;left:70px;top:0;width:162px;height:136px}
.brand svg{position:absolute;left:0;top:0}
.brand-name{position:absolute;left:0;top:56px;width:162px;text-align:center;color:var(--purple-text);font-weight:700;font-size:25px;line-height:26px}
.tagline{position:absolute;left:252px;top:18px;color:var(--white);font-weight:700;font-size:31px}
.cta{position:absolute;top:28px;height:25px;border-radius:13px;background:var(--orange);color:var(--white);font-size:15px;line-height:25px;text-align:center}
.cta-franchise{left:847px;width:151px}
.cta-stores{left:1006px;width:117px}
.mainnav{position:absolute;left:256px;top:79px;display:flex;list-style:none;font-size:16.5px;color:var(--white)}
.mainnav li{white-space:nowrap}
.mainnav li+li::before{content:"|";margin:0 14px}
.mainnav .current{color:var(--purple-text);font-weight:700}
.panel{position:absolute;left:67px;top:140px;width:1077px;height:750px;background:var(--white);border-top-right-radius:28px}
.hero{position:absolute;left:77px;top:148px;width:1058px;height:290px;border-top-left-radius:18px;border-top-right-radius:18px;
  background:linear-gradient(160deg,#6b4a7e 0,#8c7a74 35%,#b3a595 60%,#4c3a3f 100%)}
.dots{position:absolute;left:1056px;top:409px;display:flex;gap:6px}
.dots span{width:19px;height:19px;border-radius:50%;background:#e9e9e9;border:2px solid #cfcfcf}
.dots .on{background:var(--orange);border-color:#d86c0c}
.caption{position:absolute;left:77px;top:438px;width:1058px;height:84px;background:var(--orange-deep);color:var(--white);padding:12px 13px;font-size:14.5px;line-height:18px}
.caption strong{display:block;font-size:16px}
.stripe{position:absolute;left:77px;top:522px;width:1058px;height:20px;background:repeating-linear-gradient(135deg,#b5b5b5 0 2px,#d8d8d8 2px 5px)}
.news{position:absolute;left:86px;top:564px;width:304px;font-size:14px;line-height:19.5px}
.heading{color:var(--purple-text);font-weight:700;font-size:19px;margin-bottom:9px}
.news .heading{display:flex;align-items:center;gap:8px}
.news p+p{border-top:1px dotted #bbb;margin-top:10px;padding-top:10px}
.divider{position:absolute;left:408px;top:552px;width:1px;height:228px;background:var(--rule)}
.welcome{position:absolute;left:430px;top:568px;width:700px;font-size:14.5px;line-height:19.5px}
.welcome p+p{margin-top:19px}
.clients{position:absolute;left:84px;top:787px;width:1040px;height:88px;border-top:1px solid var(--rule)}
.clients-label{position:absolute;left:0;top:0;width:22px;height:88px;background:var(--purple-text);color:var(--white);font-size:13px;writing-mode:vertical-rl;transform:rotate(180deg);text-align:center;line-height:22px}
.client-list{position:absolute;left:40px;top:0;right:0;height:88px;display:flex;justify-content:space-between;align-items:center;list-style:none;font-weight:700;font-size:17px;color:#4d4d4d}
.footer{position:absolute;left:71px;top:904px;font-size:14px;line-height:21px;color:#333}
.footer a{color:#333}
.social{position:absolute;left:1030px;top:909px;display:flex;gap:8px;font-size:13px;color:#3b5c8c;font-weight:700}
.social span{display:flex;align-items:center;gap:4px}
.social i{width:12px;height:12px;background:#3b5c8c;display:inline-block}
</style>
</head>
<body>
<header>
  <div class="topbar"></div>
  <div class="navbar"></div>
  <div class="brand">
    <svg width="162" height="136" viewBox="0 0 162 136"><path d="M0 0H162V118L81 136L0 118Z" fill="#f07d12"/></svg>
    <div class="brand-name">Marlow<br>Wraps</div>
  </div>
  <div class="tagline">It's how we roll</div>
  <a class="cta cta-franchise">Franchise Enquiry</a>
  <a class="cta cta-stores">Store Locator</a>
  <ul class="mainnav">
    <li class="current">Home</li><li>Health/Nutrition</li><li>Store Locator</li><li>Products</li><li>Leasing</li><li>Partners</li><li>About Us</li><li>Contact Us</li>
  </ul>
</header>
<main>
  <div class="panel"></div>
  <div class="hero" role="img" aria-label="Photo of a busy wrap shop counter with staff, rotisserie grills and lit menu boards"></div>
  <div class="dots"><span class="on"></span><span></span><span></span></div>
  <div class="caption"><strong>Lorem ipsum dolor sit amet, consectetur adipiscing elit. Proin est tortor, pulvinar vel ullam corperut</strong>Porttitor non ante. Nam bibendum mi sit amet ipsum pulvinar volutpat. Aenean blandit iaculis tellus, non dapibus est vehicula n. Sed a neque metus luctus ligula. Cras id neque velit, id pulvinar velit. Integer eu nisi at massa consectetur adipiscing elit.</div>
  <div class="stripe"></div>
  <section class="news">
    <h2 class="heading"><svg width="17" height="17" viewBox="0 0 17 17"><circle cx="8" cy="8" r="6" fill="none" stroke="#888" stroke-width="2"/><path d="M11 12l4 4" stroke="#888" stroke-width="2"/></svg>What's New</h2>
    <p>Lorem ipsum dolor sit amet, consectetur adipi tyu scing elit. Proin est tortor, pulvinar vel uam ishjuk&nbsp; corper ut, porttitor non is&nbsp; ante.</p>
    <p>Nabib uiyhd sec endum mi sit amet ipsum pulvinar volut patam bib uiyhd endum mi sit amet ipsm pulvinar volutpat. Endum mi sit amet ipsum pulvinar volut patam.</p>
  </section>
  <div class="divider"></div>
  <section class="welcome">
    <h1 class="heading">Welcome to Marlow Wraps</h1>
    <p>In 1989, Mr Sam Dorell launched the first Marlow Wrap (MW) shop in Lakeside Plaza Shopping Centre, Loganholme Queensland. Queenslanders had not yet seen nor heard of a wrap. After a fierce sampling exercise, Queenslanders embraced Marlow Wraps. It was a roaring success. To this day Marlow at Lakeside, is recognised as one of the most successful wrap retail shops in the country.</p>
    <p>Within 3 years Marlow Wraps was operating in 4 locations between the Gold Coast and Brisbane. Lorem ipsum dolor sit amet, consectetur adipi tyu scing elit. Proin est tortor, pulvinar vel uam ishjuk corper ut, porttitor non is&nbsp; ante.</p>
  </section>
  <section class="clients">
    <div class="clients-label">Our Clients</div>
    <ul class="client-list">
      <li>Northway</li><li>Carewell</li><li>Limewood</li><li>Pactline</li><li>Starlot</li><li>Forthmore</li><li>Redhill Club</li><li>Fuelstar</li><li>Kestrix</li>
    </ul>
  </section>
</main>
<footer>
  <div class="footer">
    T: +61 7 3000 4120&nbsp; |&nbsp; F: +61 7 3000 4121&nbsp; |&nbsp; E: info@tallowwraps.com.au<br>
    <a href="#">Terms Of Use</a>&nbsp; |&nbsp; <a href="#">Privacy Statement</a>&nbsp;&nbsp; Copyright © 2011 Marlow Wraps. All rights reserved.
  </div>
  <div class="social"><span><i></i>Friendly</span><span><i></i>Chirp</span></div>
</footer>
</body>
</html>
```